Wandeln statt warten - Flyer-Design für einen bahnbrechenden Workshop
Zielgruppe
Wir sind die Exzellenz in Faciliation - wir bringen Menschen so zusammen, dass etwas vollkommen Neues entsteht. Und wir bilden Menschen in dieser Kunst aus.
Aufgabenstellung
Mit unserem Workshop „Klar gestalten!“ begehen wir Neuland, für uns wie für unsere Kunden. Das wollen wir mit einem Flyer-Layout zum Ausdruck bringen.
Das Layout soll die bestehende KERO-CI weiterentwickeln. Insbesondere verzichten wir auf den im bisherigen CI abgelegten Bilder. Veränderbar sind sowohl Schriftarten als auch Layout-Elemente
Das Layout sollte generisch sein und die Grundlage für weitere Veranstaltungsflyer sein.
Uns schwebt ein reduziertes, konzentriertes Layout vor, bei dem der Inhalt wirken kann.
Zur Orientierung liegt der aktuelle Entwurf für unsere Homepage bei.
Die im Text angegebenen Inhalte müssen nicht alle im Flyer abgebildet werden. Der Designer/die Designerin kann eine Auswahl treffen der Inhalte, die sie für wichtig hält.
Zentral aber sind: Einführungspreis, Ort und Termin
Der Flyer ist ausschließlich zur digitalen Verteilung vorgesehen.

```html
<!DOCTYPE html>
<html lang="de">
<head>
<meta charset="utf-8">
<title>Klar gestalten! – Workshop-Flyer</title>
<link href="https://fonts.googleapis.com/css2?family=Open+Sans:wght@300;400;600;700&display=swap" rel="stylesheet">
<style>
  :root {
    --stage: #6b6b6b;
    --paper: #ffffff;
    --red: #e8474a;
    --maroon: #6b1f2e;
    --dark: #333333;
    --text: #3a3a3a;
  }
  * { box-sizing: border-box; margin: 0; padding: 0; }
  html, body { width: 1200px; height: 900px; overflow: hidden; }
  body { background: var(--stage); font-family: "Open Sans", Arial, sans-serif; color: var(--text); position: relative; }
  .page { position: absolute; top: 78px; width: 526px; height: 744px; background: var(--paper); overflow: hidden; }
  .page--one { left: 55px; }
  .page--two { left: 619px; }
  .page::before { content: ""; position: absolute; left: 0; top: 0; right: 0; height: 6px; background: var(--red); }
  .page::after { content: ""; position: absolute; left: 0; bottom: 0; width: 100%; height: 7px; background: linear-gradient(90deg, var(--maroon) 0 70%, var(--dark) 70% 100%); }
  .page-label { position: absolute; top: 847px; font-size: 12px; color: #fff; }
  .abs { position: absolute; }
  .brand { text-align: center; }
  .brand__circle { width: 62px; height: 62px; border-radius: 50%; background: var(--red); margin: 0 auto; }
  .brand__name { font-size: 10px; letter-spacing: 2px; color: var(--dark); margin-top: 10px; }
  .frame { position: absolute; border-style: solid; border-width: 0; }
  .frame--red { border-color: var(--red); border-top-width: 4px; border-right-width: 4px; }
  .frame--maroon { border-color: var(--maroon); border-left-width: 4px; border-bottom-width: 4px; }
  .frame--dark { border-color: var(--dark); border-right-width: 4px; border-bottom-width: 4px; }
  .title { font-size: 22px; font-weight: 700; color: var(--red); text-align: right; }
  .subtitle { font-size: 12.5px; font-weight: 600; color: var(--red); text-align: right; white-space: nowrap; }
  .tagline { font-size: 8.5px; color: var(--red); text-align: right; line-height: 1.4; }
  .copy { font-size: 8.3px; font-weight: 300; line-height: 1.6; }
  .copy b { font-weight: 700; }
  .copy--right { text-align: right; }
  .copy--red { color: var(--red); }
  .lead { font-size: 8.6px; font-weight: 600; line-height: 1.6; text-align: right; color: var(--dark); }
  .heading-small { font-size: 8.8px; font-weight: 700; color: var(--dark); }
  .checklist { list-style: none; font-size: 8.4px; font-weight: 300; }
  .checklist li { display: flex; align-items: flex-start; gap: 8px; line-height: 15.6px; white-space: nowrap; }
  .checklist svg { width: 8px; height: 8px; flex: none; margin-top: 4px; }
  .checklist--right li { justify-content: flex-end; }
  .checklist--red { color: var(--red); }
  .checklist--maroon { color: var(--maroon); }
  .section-red { font-size: 13.5px; font-weight: 700; color: var(--red); }
  .day { display: flex; align-items: center; gap: 8px; font-size: 13.5px; font-weight: 700; color: var(--dark); }
  .day svg { width: 22px; height: 20px; }
  .numbered { list-style: none; font-size: 8.5px; }
  .numbered li { display: flex; align-items: center; gap: 7px; height: 18px; }
  .num { width: 11px; height: 11px; border-radius: 50%; background: var(--dark); color: #fff; font-size: 6.5px; font-weight: 700; font-style: normal; display: flex; align-items: center; justify-content: center; flex: none; }
  .dims-title { font-size: 9.5px; font-weight: 700; color: var(--dark); text-align: center; }
  .dims-row { display: flex; justify-content: center; gap: 10px; font-size: 8.5px; font-weight: 700; color: var(--maroon); }
  .dims-row span { display: flex; align-items: center; gap: 4px; }
  .dims-row .num { background: var(--maroon); }
  .dates-label { font-size: 8.8px; font-weight: 700; color: var(--maroon); }
  .dates { font-size: 8.6px; color: var(--maroon); }
  .ticket { background: var(--maroon); color: #fff; padding: 4px 6px; }
  .ticket__note { font-size: 6.5px; font-weight: 700; }
  .ticket__price { font-size: 27px; font-weight: 700; line-height: 1; }
  .ticket__small { font-size: 5.5px; border-bottom: 1px solid #fff; width: 72px; }
  .intro-price { border: 1px dashed var(--maroon); color: var(--maroon); text-align: center; padding: 4px; }
  .intro-price__label { font-size: 8px; font-weight: 700; }
  .intro-price__value { font-size: 21px; font-weight: 700; }
  .contact { font-size: 8.6px; color: var(--maroon); display: flex; align-items: center; gap: 5px; white-space: nowrap; }
  .contact svg { width: 8px; height: 8px; }
  .trainer { text-align: center; color: var(--maroon); }
  .trainer__label { font-size: 8.8px; font-weight: 700; color: var(--dark); }
  .trainer__photo { width: 78px; height: 78px; border-radius: 50%; border: 3px solid var(--maroon); margin: 12px auto 8px; background: radial-gradient(circle at 50% 40%, #d9c7b8, #8b8b8b 75%); }
  .trainer__name { font-size: 11px; font-weight: 600; }
  .trainer__role { font-size: 8.5px; }
  .trainer__note { font-size: 6.5px; }
  .divider { position: absolute; width: 1px; background: var(--maroon); }
</style>
</head>
<body>
<svg width="0" height="0" style="position:absolute" aria-hidden="true">
  <symbol id="tick" viewBox="0 0 10 10">
    <rect x="0.6" y="0.6" width="8.8" height="8.8" fill="none" stroke="currentColor" stroke-width="1.2"/>
    <path d="M2.5 5.2 L4.3 7 L7.6 3.2" fill="none" stroke="currentColor" stroke-width="1.4"/>
  </symbol>
  <symbol id="calendar" viewBox="0 0 22 20">
    <rect x="1" y="3" width="20" height="16" rx="2" fill="none" stroke="currentColor" stroke-width="1.5"/>
    <path d="M1 8 H21 M6 1 V5 M16 1 V5 M5 12 H13 M5 15 H17" stroke="currentColor" stroke-width="1.5"/>
  </symbol>
</svg>

<section class="page page--one">
  <div class="abs brand" style="left:36px;top:34px;width:70px">
    <div class="brand__circle"></div>
    <div class="brand__name">KERO</div>
  </div>

  <h1 class="abs title" style="right:42px;top:36px">Wirksam werden!</h1>
  <p class="abs subtitle" style="right:42px;top:66px">Klar gestalten! Das Prinzip von „Wandeln statt warten“</p>
  <p class="abs tagline" style="right:42px;top:84px;width:340px">Wie du Teil der großen Wende wirst und andere Menschen in ihre transformative Kraft begleitest</p>

  <div class="frame frame--red" style="left:415px;top:121px;width:72px;height:156px"></div>

  <div class="abs" style="left:65px;top:143px;width:398px">
    <p class="lead">Ist es auch für dich Zeit zum Handeln? Möchtest Du auch nicht mehr auf andere warten, sondern die große Wende hin zu einem lebensfördernden Menschsein selbst gestalten?</p>
    <p class="copy copy--right" style="margin-top:10px">Der Workshop <b>„Wandeln statt warten“</b> stellt dir dafür den notwendigen Rahmen zur Verfügung. Er spannt den Bogen vom <b>„Was“ (sollen wir tun?)</b> zum <b>„Wie“ (sollen wir handeln?)</b> und bietet ein reiches Spektrum an Methoden und Ansätzen, um Menschen in ihre transformative Kraft zu bringen.</p>
    <p class="copy copy--right" style="margin-top:10px">Dieser Intensiv-Workshop führt dich in die Prinzipien und die Methodik von <b>„Wandeln statt warten“</b> ein. Dabei erfährst du die Wirksamkeit des Ansatzes in der Auseinandersetzung und Begegnung mit dir selbst.</p>
  </div>

  <p class="abs heading-small" style="left:66px;top:289px">Der Workshop beinhaltet unter anderem folgende Themen:</p>
  <ul class="abs checklist" style="left:66px;top:309px;width:400px">
    <li><svg><use href="#tick"/></svg>Warum wir mehr als nachhaltig sein können und müssen</li>
    <li><svg><use href="#tick"/></svg>Die sieben Schritte zur Wirksamkeit</li>
    <li><svg><use href="#tick"/></svg>Die vier Dimensionen des Erneuerns</li>
    <li><svg><use href="#tick"/></svg>Den Anfang im Ende erkennen: Wir wir Projekte gut aufsetzen</li>
    <li><svg><use href="#tick"/></svg>Räume des Wandels schaffen</li>
    <li><svg><use href="#tick"/></svg><span>Körperübungen und Methoden zur Arbeit mit Blockaden, zur Zielklärung und zur<br>Entscheidungsfindung</span></li>
  </ul>

  <div class="frame frame--maroon" style="left:42px;top:396px;width:238px;height:107px"></div>
  <p class="abs copy" style="left:66px;top:431px;width:418px">Der Workshop ist für Menschen, die die menschengemachten Krisen lösen wollen. Für alle, die nicht mehr an die Mär vom ewigen wirtschaftlichen Wachstum glauben, sondern die neue Gesellschaft mitgestalten und dabei ihre eigene Wirksamkeit erhöhen wollen. Für politisch Aktive, Erneuerer der Bürgergesellschaft, Menschen, die mit Menschen arbeiten (wie Coaches und Facilitatoren).</p>

  <div class="frame frame--dark" style="left:250px;top:587px;width:230px;height:116px"></div>

  <p class="abs dates-label" style="left:72px;top:523px">Termine:</p>
  <p class="abs dates" style="left:72px;top:538px">20.9.-22.9. in München &nbsp;&nbsp;| &nbsp;&nbsp;11.-13.10.19 in Köln</p>

  <div class="abs ticket" style="left:72px;top:562px;width:103px;height:60px">
    <div class="ticket__note">für Fruhbucher (bis 31.8.)</div>
    <div class="ticket__price">600 €</div>
    <div class="ticket__small">inkl. Mwst.</div>
  </div>
  <div class="abs intro-price" style="left:176px;top:562px;width:105px;height:60px">
    <div class="intro-price__label">Einführungspreis</div>
    <div class="intro-price__value">750 €</div>
  </div>

  <p class="abs dates-label" style="left:72px;top:636px">Anmeldung:</p>
  <p class="abs contact" style="left:72px;top:650px">
    <svg viewBox="0 0 10 8"><rect x="0.5" y="0.5" width="9" height="7" fill="none" stroke="currentColor"/><path d="M0.5 0.5 L5 4.5 L9.5 0.5" fill="none" stroke="currentColor"/></svg>
    info@kero-werkstatt.de &nbsp;oder&nbsp;
    <svg viewBox="0 0 10 10"><circle cx="5" cy="5" r="4.4" fill="none" stroke="currentColor"/><path d="M3.3 3 L4.2 2.8 L4.7 4 L4.2 4.5 Q4.8 5.7 5.6 6 L6.1 5.5 L7.2 6 L7 6.9 Q4 6.8 3.3 3Z" fill="currentColor"/></svg>
    08131/5550142
  </p>

  <div class="abs trainer" style="left:275px;top:520px;width:200px">
    <p class="trainer__label">Dein Trainer :</p>
    <div class="trainer__photo" role="img" aria-label="Porträtfoto des Trainers"></div>
    <p class="trainer__name">Lukas Ebersberg,</p>
    <p class="trainer__role">Begründer von Wandeln statt warten.</p>
    <p class="trainer__note">Begeisteter und inspirierender Facilitator.</p>
  </div>
</section>

<section class="page page--two">
  <p class="abs dims-title" style="left:0;right:0;top:20px"># Die Vier Dimension der Erneuerung :</p>
  <ul class="abs numbered" style="left:68px;top:38px">
    <li><span class="num">1</span>Im Leben sein</li>
    <li><span class="num">2</span>Die Angst durchqueren</li>
    <li><span class="num">3</span>Der Frage lauschen</li>
  </ul>
  <ul class="abs numbered" style="left:210px;top:38px">
    <li><span class="num">4</span>In Verbindung gehen</li>
    <li><span class="num">5</span>Dem Impuls lauschen</li>
    <li><span class="num">6</span>Den Anfang im Ende erkennen</li>
  </ul>
  <ul class="abs numbered" style="left:372px;top:38px">
    <li><span class="num">7</span>Wirksam werden</li>
  </ul>

  <p class="abs section-red" style="left:68px;top:108px">Workshop-Ablauf :</p>
  <div class="frame frame--red" style="left:222px;top:114px;width:265px;height:162px"></div>
  <p class="abs section-red" style="right:56px;top:129px;font-weight:600">Vorabend 17 – 21 Uhr</p>
  <p class="abs copy copy--right copy--red" style="right:62px;top:152px;width:330px">Wir beginnen mit dem, wo wir gerade im Leben stehen. Wir lernen einander kennen und erhalten Einblick in den Grundansatz von „Wandeln statt warten“. Wir begegnen unserer Angst und erfahren, wie wir sie fruchtbar machen können.</p>
  <ul class="abs checklist checklist--right checklist--red" style="right:62px;top:198px;width:380px">
    <li>Begrüßung<svg><use href="#tick"/></svg></li>
    <li>Schritt 1: Im Leben sein<svg><use href="#tick"/></svg></li>
    <li>Wieso Nachhaltigkeit nicht ausreicht und inwiefern wir mehr bewirken können<svg><use href="#tick"/></svg></li>
    <li>Schritt 2: Die Angst durchqueren<svg><use href="#tick"/></svg></li>
    <li>Wie wir unsere Angst fruchtbar machen<svg><use href="#tick"/></svg></li>
    <li>Abschluss &amp; Meditation<svg><use href="#tick"/></svg></li>
  </ul>

  <div class="abs day" style="left:68px;top:292px"><svg><use href="#calendar"/></svg>1. Tag</div>
  <p class="abs copy" style="left:68px;top:318px;width:400px">Der erste Tag ist den Methoden von „Wandeln statt warten“ gewidmet. Eine Morgenmeditation ermöglicht uns die Begegnung mit uns selbst. Wir erforschen die zentralen Ansätze von „Wandeln statt warten“ und erlernen die Kunst der Fragen, die ändern. Wir öffnen für uns selbst Räume des Wandels und lernen, diese auch anderen Menschen zu eröffnen.</p>

  <div class="frame frame--maroon" style="left:40px;top:345px;width:210px;height:138px"></div>
  <ul class="abs checklist checklist--maroon" style="left:68px;top:384px">
    <li><svg><use href="#tick"/></svg>Begrüßung und Morgenmeditation</li>
    <li><svg><use href="#tick"/></svg>Schritt 3: Der Frage lauschen</li>
    <li><svg><use href="#tick"/></svg>Die Kunst des Fragens</li>
    <li><svg><use href="#tick"/></svg>Die sieben Schritte zur Wirksamkeit</li>
    <li><svg><use href="#tick"/></svg>Schritt 4: In Verbindung gehen</li>
  </ul>
  <div class="divider" style="left:249px;top:384px;height:84px"></div>
  <ul class="abs checklist checklist--maroon" style="left:270px;top:384px">
    <li><svg><use href="#tick"/></svg>Die vier Dimensionen des Erneuerns</li>
    <li><svg><use href="#tick"/></svg>Schritt 5: Dem Impuls lauschen</li>
    <li><svg><use href="#tick"/></svg>Räume des Wandels schaffen</li>
    <li><svg><use href="#tick"/></svg>Die drei Aufgaben eines Facilitators</li>
    <li><svg><use href="#tick"/></svg>Abschluss &amp; Meditation</li>
  </ul>

  <div class="abs day" style="right:68px;top:472px;flex-direction:row-reverse"><svg><use href="#calendar"/></svg>2. Tag</div>
  <p class="abs copy copy--right" style="right:62px;top:499px;width:400px">Der zweite Tag ist uns selbst und dem Wandel gewidmet. Beide Aspekte bedingen einander. Denn Veränderung vollzieht sich nur dann, wenn wir uns selbst verändern. Wie aber kann uns das gelingen? Und wieso schützen wir uns oftmals vor Veränderungen? Wir erkennen die Bedeutung des Anfangs und wie wir lernen, unsere Arbeit richtig zu beginnen. Zum Abschluss unterstützen uns gegenseitig, den Transfer in den Alltag zu schaffen.</p>

  <div class="frame frame--dark" style="left:300px;top:548px;width:187px;height:145px"></div>

  <div class="abs brand" style="left:58px;top:571px;width:74px">
    <div class="brand__circle" style="width:64px;height:64px"></div>
    <div class="brand__name">KERO</div>
  </div>

  <ul class="abs checklist checklist--right" style="right:62px;top:572px;width:300px;color:var(--dark)">
    <li>Begrüßung und Morgenmeditation<svg><use href="#tick"/></svg></li>
    <li>Schritt 6: Den Anfang im Ende erkennen<svg><use href="#tick"/></svg></li>
    <li>Schritt 7: Wirksam werden<svg><use href="#tick"/></svg></li>
    <li>Das Zentrum: die Arbeit mit sich selbst<svg><use href="#tick"/></svg></li>
    <li>Der Schutz vor Veränderungen: Wandel wirklich verstehen<svg><use href="#tick"/></svg></li>
    <li>Abschluss<svg><use href="#tick"/></svg></li>
  </ul>

  <p class="abs dims-title" style="left:0;right:0;top:693px"># Die Vier Dimension der Erneuerung :</p>
  <div class="abs dims-row" style="left:0;right:0;top:712px">
    <span><i class="num">1</i>Die Mitgestaltenden</span>
    <span><i class="num">2</i>Der Ort</span>
    <span><i class="num">3</i>Die Gemeinschaft</span>
    <span><i class="num">4</i>Die Natur</span>
  </div>
</section>

<p class="page-label" style="left:303px">Pg.1</p>
<p class="page-label" style="left:890px">Pg.2</p>
</body>
</html>
```